Mobile Disc Jockey Service Brochure

We are looking for a brochure to showcase our Mobile DJ Business. It needs to be something professional looking and fit our target market of Weddings. We cater to events of all types but majority of our clients are brides looking for professional service at affordable prices.

Our website for reference: http://www.thesoundcaravan.com/
facebook for reference: https://www.facebook.com/MarcusSoundCaravan

I've uploaded a picture of us, our logo and some other photos that might be useful. Feel free to use additional stock photos that may be applicable to our project needs. Feel free to crop photos as necessary

I'd like this to be an 8 1/2" x 11" bifold, or trifold brochure, double sided. The front can be simple with our logo and phone number. Back can also be simple with a small logo and our website. I'd like one of the areas to focus on our bio and picture, and the other areas can describe our packages and what we offer as well as our mission statement

Some other information: We provide not only Professional and Enthusiastic DJ Services but we also do Uplighting as well as Event planning.

Target Market(s)

Weddings, Anniversary Parties, Birthdays, Themed Party

Industry/Entity Type

Business

Requirements
Must have
• Something describing our services like the following (feel free to rearrange the wording if necessary).
• All packages are hourly and custom built to fit your party needs. A list of our offerings includes:
• Cocktail music, dinner music, dance music
• Ultimate coordination of activities and unique event planning experience
• HD Sound
• LED Light Show
• Wireless Microphone System
• Unlimited choice of song titles from Digital to Vinyl
• Free travel within 50 miles - Travel outside of this is calculated with a fee per additional mile.
• Optional Services:
• Projector with Screen for Slide Shows & Movies
• Uplighting
• We provide a Fun & Easy to use web interface that walks you through the timeline of your event capturing every detail you desire, making planning fun! We guarantee you will hear everything you want, we have an endless music library as well as mobile internet so we can access any song you and your guests want instantly! In addition to the Online Event Planner, we offer unlimited consultations prior to your event to ensure face to face that you are getting everything you want and more.
• I'd like to see something featuring our services as well as our picture that I uploaded maybe cropped at the chest level or there abouts with this information:
• We are a husband and wife team. Marcus Halloway, the DJ has been providing custom soundtracks for events of all types for well over a decade. In 2011 his wife Tessa joined the team to handle all of the event coordination and logistics. Together we run the Sound Caravan offering Professional DJ Services at a personal level. We enjoy working with clients to create the event that they deserve at an affordable price. Contact us today for your quote or visit us online.
• (555) 314-2086
• thesoundcaravan@mailbox-example.com
• www.thesoundcaravan.com
• www.facebook.com/MarcusSoundCaravan
• Id also like something along the lines of:
• Your choice of DJ can make or break your event. The Sound Caravan guarantees to go above and beyond to make your event flawless and unforgettable. We promise to provide nothing but the best, well within your budget. When it comes to Weddings, we recognize that your Wedding is the most important day of your life! We will work with you side by side to ensure that it's everything you have dreamed of and more. Let the experience we provide create a beautiful memory that will last a lifetime.
• (Mission Statement)
• Our mission is to provide high quality and affordable mobile DJ services that will fill your event with beautiful lifelong memories.
Nice to have
• Id like to see the picture of the bride and grandfather dancing put in there somewhere.
• Color Scheme should be a mix of greys, black, white, you can add color as needed to match photos/logo, etc.

```html
<!DOCTYPE html>
<html lang="en">
<head>
<meta charset="utf-8">
<title>The Sound Caravan – Brochure Inside</title>
<link href="https://fonts.googleapis.com/css2?family=Marck+Script&family=Questrial&family=Mulish:wght@700&display=swap" rel="stylesheet">
<style>
  :root{
    --brand-red:#a81c22;
    --script-red:#b3232b;
    --ink:#111111;
    --paper:#ffffff;
    --panel-dark:#000000;
    --panel-light:#9c9c9c;
    --photo-mid:#6f6f6f;
  }
  html,body{margin:0;padding:0;overflow:hidden;background:var(--paper);}
  .canvas{position:relative;width:1200px;height:1000px;background:var(--paper);overflow:hidden;}
  .bio-panel{position:absolute;left:12px;top:43px;width:400px;height:914px;background:var(--brand-red);}
  .portrait-frame{position:absolute;left:55px;top:64px;width:288px;height:368px;background:var(--paper);}
  .portrait{position:absolute;left:12px;top:14px;width:264px;height:340px;background:linear-gradient(160deg,#3a3a3a,#8a8a8a 55%,#2c2c2c);}
  .bio-text{position:absolute;left:10px;top:455px;width:380px;margin:0;text-align:center;
    font-family:"Marck Script",cursive;font-size:24.5px;line-height:31.5px;color:var(--ink);}
  .offer-panel{position:absolute;left:412px;top:43px;width:776px;height:914px;}
  .offer-art{position:absolute;left:0;top:0;}
  .script-heading{position:absolute;margin:0;font-family:"Marck Script",cursive;font-weight:400;color:var(--script-red);}
  .services-heading{left:66px;top:402px;font-size:40px;}
  .services-list{position:absolute;left:38px;top:454px;width:300px;margin:0;padding:0;list-style:none;text-align:center;
    font-family:"Questrial",sans-serif;font-size:15.5px;line-height:21px;color:var(--paper);}
  .services-list strong{font-family:"Mulish",sans-serif;font-weight:700;font-size:15.5px;}
  .optional-title{display:block;margin-top:19px;font-family:"Mulish",sans-serif;font-weight:700;text-decoration:underline;}
  .packages-note{position:absolute;left:30px;top:820px;width:320px;margin:0;text-align:center;
    font-family:"Marck Script",cursive;font-size:25px;line-height:30px;color:var(--script-red);}
  .easy-heading{left:423px;top:512px;font-size:40px;line-height:40px;}
  .easy-heading span{display:block;padding-left:12px;}
  .easy-text{position:absolute;left:420px;top:602px;width:306px;margin:0;text-align:center;
    font-family:"Questrial",sans-serif;font-size:15.5px;line-height:21.7px;color:var(--ink);}
</style>
</head>
<body>
<main class="canvas">
  <section class="bio-panel">
    <div class="portrait-frame">
      <div class="portrait" role="img" aria-label="Black and white photo of the husband and wife DJ team standing together outdoors"></div>
    </div>
    <p class="bio-text">We are a husband and wife team.<br>Marcus Halloway, the DJ has been<br>providing custom soundtracks for<br>events of all types for well over a<br>decade. In 2011 his wife Tessa joined<br>the team to handle all of the event<br>coordination and logistics. Together<br>we run the Sound Caravan offering<br>Professional DJ Services at a personal<br>level. We enjoy working with clients to<br>create the event that they deserve at<br>an affordable price. Contact us today<br>for your quote or visit us online.</p>
  </section>

  <section class="offer-panel">
    <svg class="offer-art" width="776" height="914" viewBox="0 0 776 914">
      <defs>
        <linearGradient id="panelFade" x1="0" y1="0" x2="0" y2="1">
          <stop offset="0.48" stop-color="var(--panel-dark)"/>
          <stop offset="1" stop-color="var(--panel-light)"/>
        </linearGradient>
        <linearGradient id="photoTone" x1="0" y1="0" x2="1" y2="1">
          <stop offset="0" stop-color="#2a2a2a"/>
          <stop offset="0.45" stop-color="var(--photo-mid)"/>
          <stop offset="1" stop-color="#3a3a3a"/>
        </linearGradient>
      </defs>
      <rect width="776" height="914" fill="url(#panelFade)"/>
      <path role="img" aria-label="Black and white photo of wedding guests dancing on a crowded dance floor"
            d="M6 14 Q380 180 776 6 L776 606 Q700 560 620 520 Q430 400 6 336 Z" fill="url(#photoTone)"/>
      <path d="M0 0 L776 0 L776 6 Q380 180 6 14 L0 14 Z" fill="var(--panel-dark)"/>
      <path d="M560 480 Q690 540 776 614" fill="none" stroke="var(--panel-dark)" stroke-width="8"/>
    </svg>

    <h2 class="script-heading services-heading">Our Services</h2>
    <ul class="services-list">
      <li><strong>Cocktail music, dinner music,<br>dance music</strong></li>
      <li>Ultimate coordination of activities and<br>unique event planning experience</li>
      <li><strong>HD Sound</strong></li>
      <li>LED Light Show</li>
      <li><strong>Wireless Microphone System</strong></li>
      <li>Unlimited choice of song titles from<br>Digital to Vinyl</li>
      <li><strong>Free travel within 50 miles</strong></li>
      <li>Travel outside of this is calculated with<br>a fee per additional mile.</li>
      <li><span class="optional-title">Optional Services</span></li>
      <li>Projector with screen for slideshows<br>and movies</li>
      <li>Uplighting</li>
    </ul>
    <p class="packages-note">All packages are hourly and<br>custom built to fit your party needs</p>

    <h2 class="script-heading easy-heading">Making it<span>Easy for You</span></h2>
    <p class="easy-text">We provide a Fun &amp; Easy to use web interface that walks you through the timeline of your event capturing every detail you desire, making planning fun! We guarantee you will hear everything you want, we have an endless music library as well as mobile internet so we can access any song you and your guests want instantly! In addition to the Online Event Planner, we offer unlimited consultations prior to your event to ensure face to face that you are getting everything you want and more.</p>
  </section>
</main>
</body>
</html>
```